Sales Tip from Ned Valcourt- Think Like a Buyer-

I am a sales trainer for B2B sales teams. I would like you to create an infographic that my learners can view, easily understand and immediately apply to their day to day work.
The graphic should:
1-Display the title on top- Sales Tip from Ned Valcourt- Think Like a Buyer
2- Please use the writing and layout from the attachment.
3- Create a tagline at the bottom that says- Top B2B Sales Teams, Sell The Way Thier Clients Buy.
Our company colors are red, silver with slight black trim.
I do not like cartoon like graphics. This must be poweful...
Updates

thank you very much for your consideration. looking forward to seeing your work Ned

Target Market(s)

CEO's of B2B Technology Companies

Font styles to use
Sans Serif

Requirements
Must have
• the apility to attach to a powerpoint slide. company colors...red, silver and a little black
Should not have
• cartoon animation, business,

```html
<!DOCTYPE html>
<html lang="en">
<head>
<meta charset="utf-8">
<title>Sales Tip from Ned Valcourt – Think Like a Buyer</title>
<link rel="stylesheet" href="https://fonts.googleapis.com/css2?family=Montserrat:wght@300;400;500;700;800;900&family=Mulish:wght@500;600&display=swap">
<style>
  :root {
    --backdrop: #8a8a8a;
    --paper: #ffffff;
    --red: #e30613;
    --red-deep: #b3000c;
    --red-text: #c4000f;
    --ink: #111111;
    --silver-light: #f4f4f4;
    --silver: #d9d9d9;
    --rule: #1a1a1a;
  }
  * { box-sizing: border-box; margin: 0; padding: 0; }
  html, body {
    width: 902px; height: 1200px; overflow: hidden;
    background: var(--backdrop);
  }
  .poster {
    position: absolute; left: 26px; top: 0;
    width: 931px; height: 1315px;
    transform: scale(0.9125); transform-origin: 0 0;
    background: var(--paper);
  }
  .frame {
    position: absolute; left: 23px; top: 23px;
    width: 875px; height: 1269px;
    border: 2px solid var(--rule);
  }
  .header {
    position: absolute; left: 25px; top: 25px; width: 871px; height: 200px;
    background: linear-gradient(180deg, var(--red) 0%, var(--red-deep) 100%);
    color: #fff; text-align: center;
    font-family: "Montserrat", sans-serif;
    overflow: hidden;
  }
  .header-notch {
    position: absolute; left: 448px; top: 200px; width: 44px; height: 22px;
    background: var(--red-deep); border-radius: 0 0 22px 22px;
  }
  .kicker {
    position: absolute; left: 0; right: 0; top: 28px;
    font-size: 47px; font-weight: 300; letter-spacing: -0.5px;
    white-space: nowrap;
  }
  .kicker strong { font-weight: 800; }
  .headline {
    position: absolute; left: 0; right: 0; top: 80px;
    font-size: 87px; font-weight: 900; letter-spacing: -3px;
    white-space: nowrap;
    text-shadow: 0 4px 6px rgba(0,0,0,0.45);
  }
  .headline span { display: inline-block; transform: scaleX(0.85); }
  .column-bar {
    position: absolute; left: 23px; top: 278px; width: 875px; height: 67px;
    background: linear-gradient(180deg, var(--red) 0%, var(--red-deep) 100%);
    border-radius: 34px;
    font-family: "Montserrat", sans-serif; font-weight: 800;
    font-size: 32px; color: #fff;
  }
  .column-bar span { position: absolute; top: 13px; width: 300px; text-align: center; }
  .column-bar .seller { left: 83px; }
  .column-bar .buyer { left: 527px; }
  .column-divider {
    position: absolute; left: 461px; top: 280px; width: 2px; height: 829px;
    background: var(--rule);
  }
  .table-bottom {
    position: absolute; left: 23px; top: 1107px; width: 875px; height: 2px;
    background: var(--rule);
  }
  .tip {
    position: absolute; font-family: "Mulish", sans-serif; font-weight: 600;
    font-size: 35px; line-height: 49px; color: var(--ink);
    white-space: nowrap;
  }
  .tip-number {
    position: absolute; width: 38px; height: 38px; border-radius: 50%;
    background: var(--red); color: #fff;
    font-family: "Montserrat", sans-serif; font-weight: 800; font-size: 21px;
    line-height: 38px; text-align: center;
  }
  .seller-col .tip { left: 115px; }
  .seller-col .tip-number { left: 56px; }
  .buyer-col .tip { left: 537px; }
  .buyer-col .tip-number { left: 480px; }
  .footer {
    position: absolute; left: 25px; top: 1147px; width: 871px; height: 143px;
    background: linear-gradient(180deg, var(--silver-light) 0%, var(--silver) 100%);
    text-align: center; font-family: "Montserrat", sans-serif;
  }
  .footer-notch {
    position: absolute; left: 442px; top: 1125px; width: 46px; height: 23px;
    background: var(--silver-light); border-radius: 23px 23px 0 0;
  }
  .tagline-lead {
    position: absolute; left: 0; right: 0; top: 30px;
    font-size: 47px; font-weight: 900; color: var(--ink); letter-spacing: -0.5px;
    white-space: nowrap;
  }
  .tagline-close {
    position: absolute; left: 0; right: 0; top: 82px;
    font-size: 46px; font-weight: 500; color: var(--red-text);
    white-space: nowrap;
  }
</style>
</head>
<body>
  <div class="poster">
    <div class="frame"></div>

    <header class="header">
      <div class="kicker">SALES TIP FROM <strong>NED VALCOURT</strong></div>
      <h1 class="headline"><span>THINK LIKE A BUYER</span></h1>
    </header>
    <div class="header-notch"></div>

    <div class="column-bar">
      <span class="seller">SELLER</span>
      <span class="buyer">BUYER</span>
    </div>
    <div class="column-divider"></div>
    <div class="table-bottom"></div>

    <section class="seller-col">
      <div class="tip-number" style="top:393px">1</div>
      <p class="tip" style="top:388px">Do they like us?</p>
      <div class="tip-number" style="top:479px">2</div>
      <p class="tip" style="top:474px">Do they like our<br>product better than<br>Competition?</p>
      <div class="tip-number" style="top:663px">3</div>
      <p class="tip" style="top:658px">Will they accept<br>our price?</p>
      <div class="tip-number" style="top:797px">4</div>
      <p class="tip" style="top:792px">Are we close it<br>quickly W/o being<br>too pushy?</p>
    </section>

    <section class="buyer-col">
      <div class="tip-number" style="top:393px">1</div>
      <p class="tip" style="top:388px">How will this impact<br>our business?</p>
      <div class="tip-number" style="top:528px">2</div>
      <p class="tip" style="top:523px">What risk or<br>disruptions could<br>occure?</p>
      <div class="tip-number" style="top:712px">3</div>
      <p class="tip" style="top:707px">Why do we need to<br>do this now?</p>
      <div class="tip-number" style="top:846px">4</div>
      <p class="tip" style="top:841px">Why them don’t<br>competition?</p>
      <div class="tip-number" style="top:981px">5</div>
      <p class="tip" style="top:976px">What are all costs?<br>Is it a fair deal</p>
    </section>

    <div class="footer-notch"></div>
    <footer class="footer">
      <div class="tagline-lead">TOP B2B SALES TEAMS</div>
      <div class="tagline-close">SELL THE WAY THIER CLIENTS BUY</div>
    </footer>
  </div>
</body>
</html>
```